Lena Corvell Business Card

I need a business card that reflects my current website: itslenacorvell.example and screenshot attached. If we keep the color scheme of the site and sample card below that would be ideal. The business card should include the information on the attached sample cards.

Industry/Entity Type

Business

```html
<!DOCTYPE html>
<html lang="en">
<head>
<meta charset="utf-8">
<title>Lena Corvell – Business Card</title>
<link rel="stylesheet" href="https://fonts.googleapis.com/css2?family=Ubuntu:ital,wght@0,400;0,700;1,300;1,400&display=swap">
<style>
  :root {
    --page: #ffffff;
    --field-top: #dfe3e3;
    --field-bottom: #f1f3f3;
    --slate: #8ea8b9;
    --ink-dark: #44546a;
    --mint-top: #56dd8e;
    --mint-bottom: #69f99e;
    --white: #ffffff;
    --footer-ink: #3c454f;
    --rule: #b9bfc2;
  }
  * { margin: 0; padding: 0; box-sizing: border-box; }
  html, body {
    width: 1200px; height: 686px; overflow: hidden;
    background: var(--page);
    font-family: "Ubuntu", sans-serif;
  }
  .card { position: relative; width: 1200px; height: 686px; background: var(--page); }
  .card__field {
    position: absolute; left: 25px; top: 25px; width: 1150px; height: 636px;
    background: linear-gradient(to bottom, var(--field-top) 0%, var(--field-bottom) 30%, var(--field-bottom) 100%);
  }
  .identity {
    position: absolute; left: 0; top: 175px; width: 549px; height: 353px;
    background: var(--slate);
    border-radius: 0 14px 14px 0;
  }
  .tab { position: absolute; width: 23px; height: 231px; background: var(--ink-dark); }
  .tab--left { left: 0; top: 240px; border-radius: 0 10px 10px 0; }
  .tab--right { right: 0; top: 234px; border-radius: 10px 0 0 10px; }
  .identity__name {
    position: absolute; right: 46px; top: 62px;
    font-weight: 700; font-size: 57px; letter-spacing: 1.5px;
    color: var(--white); white-space: nowrap; line-height: 1;
  }
  .identity__roles {
    position: absolute; right: 42px; top: 133px;
    list-style: none; text-align: right;
    font-style: italic; font-weight: 300; font-size: 44px; line-height: 57px;
    color: var(--white); white-space: nowrap;
  }
  .contact {
    position: absolute; left: 576px; top: 175px; width: 624px; height: 353px;
    background: linear-gradient(to bottom, var(--mint-top), var(--mint-bottom));
    border-radius: 14px 0 0 14px;
  }
  .contact__list { position: absolute; left: 41px; top: 84px; list-style: none; }
  .contact__item {
    display: flex; align-items: center; height: 60px;
    font-size: 40px; color: var(--white); white-space: nowrap;
  }
  .contact__icon { width: 42px; height: 42px; margin-right: 20px; flex: none; }
  .contact__dot {
    width: 42px; height: 42px; border-radius: 50%;
    background: var(--ink-dark); margin-right: 20px; flex: none;
  }
  .site {
    position: absolute; left: 0; right: 0; top: 592px;
    display: flex; justify-content: center; align-items: center; gap: 14px;
  }
  .site__rule { width: 290px; height: 5px; }
  .site__rule--left { background: linear-gradient(to right, rgba(185,191,194,0), var(--rule)); border-radius: 3px 0 0 3px; }
  .site__rule--right { background: linear-gradient(to left, rgba(185,191,194,0), var(--rule)); }
  .site__url { font-size: 38px; color: var(--footer-ink); white-space: nowrap; }
</style>
</head>
<body>
<main class="card">
  <div class="card__field"></div>

  <section class="identity">
    <h1 class="identity__name">LENA CORVELL</h1>
    <ul class="identity__roles">
      <li>Brand Curator</li>
      <li>Digital Storyteller</li>
      <li>Social Entrepreneur</li>
    </ul>
  </section>
  <div class="tab tab--left"></div>

  <section class="contact">
    <ul class="contact__list">
      <li class="contact__item">
        <svg class="contact__icon" viewBox="0 0 42 42" aria-hidden="true">
          <circle cx="21" cy="21" r="21" fill="var(--ink-dark)"/>
          <rect x="10" y="13" width="22" height="16" rx="1.5" fill="var(--white)"/>
          <path d="M10.5 14 L21 23 L31.5 14" fill="none" stroke="var(--ink-dark)" stroke-width="2"/>
        </svg>
        <span>me@lenacorvell.example</span>
      </li>
      <li class="contact__item">
        <svg class="contact__icon" viewBox="0 0 42 42" aria-hidden="true">
          <circle cx="21" cy="21" r="21" fill="var(--ink-dark)"/>
          <path d="M13.5 11 c1.5-1 3-1 3.8 .4 l2.3 3.8 c.7 1.2 .3 2.4-.8 3.2 l-1.3 1 c.9 2.6 3 4.7 5.5 5.6 l1-1.3 c.8-1.1 2-1.5 3.2-.8 l3.8 2.3 c1.4.8 1.4 2.3 .4 3.8 c-1.5 2.2-4 3-7 1.8 c-5.2-2-9.6-6.4-11.6-11.6 c-1.2-3-.4-5.5 1.8-7 z" fill="var(--white)"/>
        </svg>
        <span>555.014.2730</span>
      </li>
      <li class="contact__item">
        <span class="contact__dot"></span>
        <span>itslenacorvell</span>
      </li>
    </ul>
  </section>
  <div class="tab tab--right"></div>

  <footer class="site">
    <span class="site__rule site__rule--left"></span>
    <span class="site__url">www.itslenacorvell.example</span>
    <span class="site__rule site__rule--right"></span>
  </footer>
</main>
</body>
</html>
```